Business Card Design for Toriven

I've already got the logo, but I'd like to see some interesting designs.

I don't want anything to complex. I like it simple,yet innovative, like the logo.

My business is System Administration for small to medium size businesses, so that will be my main target audience.
Updates

hey all, the png has been uploaded.

Hey all,

If you are submitting the back side of the card, I'd like the top bit of the card to be Toriven Solutions and the logo, the bottom of the card the website, with a white background.

The middle I'd like to leave blank for a quote that will be printed on each card.

Thanks!

Dale

Industry/Entity Type

Business

```html
<!DOCTYPE html>
<html lang="en">
<head>
<meta charset="utf-8">
<title>Toriven Solutions – Business Card</title>
<link href="https://fonts.googleapis.com/css2?family=Source+Sans+3:wght@400;600&display=swap" rel="stylesheet">
<style>
  :root {
    --backdrop: #58585a;
    --paper: #ffffff;
    --brand-blue: #1f7fc0;
    --band-dark: #1c6fae;
    --band-light: #3d97d0;
    --sky-top: #3a9fdc;
    --sky-bottom: #1f86c8;
    --ink-grey: #555555;
    --divider: #4a4a4c;
  }
  * { margin: 0; padding: 0; box-sizing: border-box; }
  html, body {
    width: 1200px; height: 386px; overflow: hidden;
    background: var(--backdrop);
    font-family: "Source Sans 3", "Myriad Pro", Arial, sans-serif;
  }
  .canvas { position: relative; width: 1200px; height: 386px; }
  .card {
    position: absolute; top: 29px; width: 539px; height: 312px;
    border-radius: 22px; overflow: hidden; background: var(--paper);
  }
  .card--front { left: 38px; }
  .card--back { left: 607px; }

  .brand { position: absolute; display: flex; align-items: center; gap: 14px; }
  .brand__mark {
    width: 62px; height: 62px; border-radius: 50%;
    background: var(--brand-blue); flex: none;
  }
  .brand__name {
    font-size: 30px; font-weight: 600; color: var(--brand-blue);
    letter-spacing: 0.2px; white-space: nowrap;
  }
  .card--front .brand { left: 24px; top: 72px; }

  .person { position: absolute; right: 38px; top: 78px; text-align: right; }
  .person__name { font-size: 27px; font-weight: 600; color: var(--brand-blue); line-height: 1.1; }
  .person__title { font-size: 21px; color: var(--ink-grey); letter-spacing: 2px; line-height: 1.4; }

  .contact-band {
    position: absolute; left: 0; right: 0; top: 207px; bottom: 0;
    background: linear-gradient(90deg, var(--band-dark) 0%, var(--band-dark) 70%, var(--band-light) 88%, var(--band-dark) 100%);
    border-top: 7px solid var(--divider);
    color: #ffffff; font-size: 17px; line-height: 23px;
  }
  .contact-band__address { position: absolute; left: 22px; top: 18px; }
  .contact-band__online { position: absolute; right: 33px; top: 41px; text-align: right; }

  .quote-field {
    position: absolute; left: 0; right: 0; top: 0; height: 225px;
    background: linear-gradient(180deg, var(--sky-top), var(--sky-bottom));
    border-bottom: 6px solid var(--divider);
  }
  .card--back .brand { left: 24px; top: 22px; }
  .card--back .brand__mark { background: var(--paper); }
  .card--back .brand__name { color: var(--paper); }
  .website {
    position: absolute; right: 33px; bottom: 28px;
    font-size: 27px; font-weight: 600; color: var(--brand-blue);
    white-space: nowrap;
  }
</style>
</head>
<body>
<main class="canvas">
  <section class="card card--front" aria-label="Card front">
    <div class="brand">
      <span class="brand__mark"></span>
      <span class="brand__name">Toriven Solutions</span>
    </div>
    <div class="person">
      <p class="person__name">Evan Marsh</p>
      <p class="person__title">President</p>
    </div>
    <div class="contact-band">
      <p class="contact-band__address">48 Sample Lane<br>Brookvale, New York 10482<br>(555) 014-2368</p>
      <p class="contact-band__online">evan@toriven.biz<br>www.Toriven.biz</p>
    </div>
  </section>

  <section class="card card--back" aria-label="Card back">
    <div class="quote-field" role="img" aria-label="Blue field left blank for a printed quote"></div>
    <div class="brand">
      <span class="brand__mark"></span>
      <span class="brand__name">Toriven Solutions</span>
    </div>
    <p class="website">www.Toriven.biz</p>
  </section>
</main>
</body>
</html>
```